Brightnest Dwelling Stationery Design

Letterpaper, business cards, notebook, envelope A4 & A5

Target Market(s)

Business, accommodation, hotels, flexible housing

Font styles to use
Other font styles liked:
• Montserrat

Colors

Designer to choose only greyscale colors for use in the design.

Requirements
Must have
• Luxurious appearance
Keep it simple, just like the logo
Modern
Nice to have
• Tight Luxury Design
Should not have
• Illustrations
Decorative

```html
<!DOCTYPE html>
<html lang="en">
<head>
<meta charset="utf-8">
<title>Brightnest Dwelling – Business Cards</title>
<link href="https://fonts.googleapis.com/css2?family=Lato:wght@300;400;700&display=swap" rel="stylesheet">
<style>
  :root {
    --stage: #0c0c0d;
    --card: #29292b;
    --card-back: #252527;
    --panel: #1d1d1f;
    --panel-rule: #5c5c5f;
    --ink: #ececec;
    --ink-soft: #c9c9cb;
    --rule: #6a6a6d;
  }
  * { box-sizing: border-box; margin: 0; padding: 0; }
  html, body {
    width: 1200px; height: 820px; overflow: hidden;
    background: var(--stage);
  }
  .stage {
    position: relative; width: 1200px; height: 820px;
    background: radial-gradient(ellipse at 55% 40%, #1a1a1c 0%, var(--stage) 70%);
    font-family: "Lato", sans-serif; color: var(--ink);
  }
  .card {
    position: absolute; width: 520px; height: 300px;
    box-shadow: 0 18px 40px rgba(0,0,0,.65);
  }
  /* Front */
  .card--front { left: 60px; top: 380px; background: var(--card); }
  .brand {
    position: absolute; left: 196px; top: 52px;
    display: flex; align-items: center; gap: 16px;
  }
  .brand__mark {
    width: 64px; height: 64px; border: 2px solid var(--ink);
  }
  .brand__name {
    font-family: "Lato", sans-serif; font-weight: 300;
    font-size: 19px; letter-spacing: 2.5px; line-height: 1.25;
    color: var(--ink); text-transform: uppercase;
  }
  .divider {
    position: absolute; left: 218px; right: 34px; top: 170px;
    height: 1px; background: var(--rule);
  }
  .person { position: absolute; left: 36px; top: 154px; }
  .person__name {
    font-weight: 700; font-size: 17px; letter-spacing: .4px; text-transform: uppercase;
  }
  .person__role { font-weight: 400; font-size: 13px; color: var(--ink-soft); margin-top: 2px; }
  .contact {
    position: absolute; left: 36px; top: 214px;
    list-style: none; font-size: 13px; line-height: 1;
  }
  .contact li { display: flex; align-items: center; gap: 8px; margin-bottom: 7px; }
  .contact svg { width: 15px; height: 15px; flex: none; }
  .address {
    position: absolute; right: 34px; top: 186px; text-align: right;
    font-size: 13px; line-height: 1.45; font-style: normal;
  }
  /* Back */
  .card--back { left: 620px; top: 170px; background: var(--card-back); }
  .card--back::after {
    content: ""; position: absolute; inset: 0;
    border-bottom: 6px solid #3d3d40;
  }
  .back__panel {
    position: absolute; left: 42px; top: 16px; width: 268px; height: 268px;
    background: var(--panel); border: 2px solid var(--panel-rule);
  }
  .back__name {
    position: absolute; left: 336px; top: 118px;
    font-weight: 300; font-size: 21px; letter-spacing: 3px; line-height: 1.35;
    text-transform: uppercase; color: var(--ink);
  }
</style>
</head>
<body>
<main class="stage">

  <section class="card card--back" aria-label="Business card, back">
    <div class="back__panel"></div>
    <p class="back__name">Brightnest<br>Dwelling</p>
  </section>

  <section class="card card--front" aria-label="Business card, front">
    <div class="brand">
      <div class="brand__mark"></div>
      <p class="brand__name">Brightnest<br>Dwelling</p>
    </div>

    <div class="divider"></div>

    <div class="person">
      <p class="person__name">Daniel Ashford</p>
      <p class="person__role">Managing Director</p>
    </div>

    <ul class="contact">
      <li>
        <svg viewBox="0 0 16 16" fill="none" stroke="currentColor" stroke-width="1.2">
          <rect x="0.6" y="0.6" width="14.8" height="14.8" rx="2.5"/>
          <path d="M5 4c-.8.4-1 1.4-.4 2.8.8 2 2.6 3.8 4.6 4.6 1.4.6 2.4.4 2.8-.4l-1.6-1.4-1.2.6c-1-.5-2-1.5-2.4-2.4l.6-1.2z" fill="currentColor" stroke="none"/>
        </svg>
        020-555 018 342
      </li>
      <li>
        <svg viewBox="0 0 16 16" fill="none" stroke="currentColor" stroke-width="1.2">
          <rect x="0.6" y="0.6" width="14.8" height="14.8" rx="2.5"/>
          <rect x="3.5" y="5" width="9" height="6.5"/>
          <path d="M3.5 5l4.5 3.6L12.5 5"/>
        </svg>
        hello@brightnest.com
      </li>
      <li>
        <svg viewBox="0 0 16 16" fill="none" stroke="currentColor" stroke-width="1.2">
          <rect x="0.6" y="0.6" width="14.8" height="14.8" rx="2.5"/>
          <circle cx="8" cy="8" r="4.2"/>
          <path d="M3.8 8h8.4M8 3.8c-1.6 2.6-1.6 5.8 0 8.4M8 3.8c1.6 2.6 1.6 5.8 0 8.4"/>
        </svg>
        www.brightnest.com
      </li>
    </ul>

    <address class="address">
      18, Harrow Lane Street<br>
      Kingsbury City, 40217
    </address>
  </section>

</main>
</body>
</html>
```